High end boutique food product label

We are looking for a label design to be used on our range of high end food products. We don't have a design or colour scheme in mind and are interested to see what ideas are submitted.
We would like it to feel sophisticated, chic, and eye-catching.
All of our products are handmade in Australia using Australian ingredients.
The graphics for the label will need to be scaleable to be fit a variety of labels from small squat jars with labels sized 3.5cm high and 7cm wide, to tall thin bottles with labels that are 14cm high and 4.5cm wide.
We would be interested in working with the winning designer to create these different sized labels.
The label submitted for this project should be 14cm high and 4.5cm wide, it should include our logo (file supplied in .jpeg and .ai), the product name 'Extra Virgin Olive Oil' and the size '250ml'.
This is just the front label on a bottle, we are not expecting a rear label to be created currently.
You are welcome to use any fonts you think will look good but the fonts used in our logo are Allaina Medium and Bebas Kai Regular.

```html
<!DOCTYPE html>
<html lang="en">
<head>
<meta charset="UTF-8">
<title>Larkwood Pantry – Extra Virgin Olive Oil Label</title>
<link href="https://fonts.googleapis.com/css2?family=Dancing+Script:wght@500&family=Oswald:wght@500&family=Playfair+Display:wght@700&family=Libre+Baskerville&display=swap" rel="stylesheet">
<style>
  :root {
    --page: #ffffff;
    --label-bg: #eef3e1;
    --label-bg-deep: #e2ebcf;
    --gold: #c9a548;
    --brand: #4b3a2c;
    --green: #77a845;
    --green-deep: #5f8f35;
    --leaf-tint: #d5e0c0;
    --size-text: #8c8272;
  }
  * { margin: 0; padding: 0; box-sizing: border-box; }
  html, body {
    width: 1200px; height: 1200px; overflow: hidden;
    background: var(--page);
  }
  .canvas { position: relative; width: 1200px; height: 1200px; }

  .label {
    position: absolute; left: 426px; top: 60px;
    width: 348px; height: 1080px;
    border-radius: 174px 174px 0 0;
    background: linear-gradient(180deg, var(--label-bg) 0%, var(--label-bg-deep) 100%);
    overflow: hidden;
  }
  .label__frame {
    position: absolute; inset: 14px 14px 14px 14px;
    border: 2px solid var(--gold);
    border-radius: 160px 160px 0 0;
  }
  .label__pattern {
    position: absolute; inset: 0;
    background: radial-gradient(ellipse at 70% 30%, rgba(213,224,192,.55), transparent 60%),
                radial-gradient(ellipse at 25% 85%, rgba(213,224,192,.5), transparent 55%);
  }

  .brand {
    position: absolute; left: 0; right: 0; top: 110px;
    text-align: center;
  }
  .brand__dot {
    display: block; width: 26px; height: 26px; margin: 0 auto 10px;
    border-radius: 50%; background: var(--brand);
  }
  .brand__name {
    font-family: "Playfair Display", serif; font-weight: 700;
    font-size: 40px; line-height: 1.05; color: var(--brand);
  }

  .branch {
    position: absolute; left: 16px; top: 345px;
    width: 120px; height: 150px;
    border-radius: 50% 40% 50% 40%;
    background: radial-gradient(ellipse at 40% 50%, #b9c9a0 0%, rgba(185,201,160,0) 70%);
  }

  .product__grade {
    position: absolute; left: 205px; top: 528px;
    font-family: "Oswald", sans-serif; font-weight: 500;
    font-size: 27px; line-height: 1; letter-spacing: 1px;
    color: var(--green); text-align: right;
  }
  .product__name {
    position: absolute; left: 30px; top: 560px;
    font-family: "Dancing Script", cursive; font-weight: 500;
    font-size: 150px; line-height: 1; color: var(--green);
  }
  .product__type {
    position: absolute; left: 176px; top: 688px;
    width: 112px; height: 40px;
    background: var(--green-deep);
    font-family: "Oswald", sans-serif; font-weight: 500;
    font-size: 30px; line-height: 40px; text-align: center;
    color: var(--label-bg);
  }

  .volume {
    position: absolute; left: 0; right: 0; top: 1000px;
    text-align: center;
    font-family: "Libre Baskerville", serif;
    font-size: 19px; color: var(--size-text);
  }
</style>
</head>
<body>
<main class="canvas">
  <section class="label" aria-label="Extra virgin olive oil front label">
    <div class="label__pattern" role="img" aria-label="Faint olive leaf pattern across the label background"></div>
    <div class="label__frame"></div>

    <header class="brand">
      <span class="brand__dot"></span>
      <div class="brand__name">Larkwood<br>Pantry</div>
    </header>

    <div class="branch" role="img" aria-label="Illustrated olive branch with leaves"></div>

    <div class="product__grade">EXTRA<br>VIRGIN</div>
    <div class="product__name">Olive</div>
    <div class="product__type">OIL</div>

    <p class="volume">250ml e 8.45 fl oz</p>
  </section>
</main>
</body>
</html>
```